Massage Therapy Business Card

I’d like the same exact business card (same graphics and colors) that I uploaded by R & K Designer with:
Name of the business: Bodywork by Delmar;
Delmar Hollis (Massage Therapist);
Contact: (555)-418-2073
Email: bodyworkbydelmar@quillmail.test;
IG: @Gr4in_bodywork

On the back Please add:
1. Mobile Sessions available upon request
2. Book 3 Massages, Get 4th 50% off

Target Market(s)

Adults ages 21+

Industry/Entity Type

Healthcare and Therapy

Contact Information for Business Card

The color should be different shades of blue with a logo of a male anatomy and pressure points for massages

Colors
0054AA
0677BA
7BADD7
CADEEF
E8F1F8
0094D4
00A9DD
6FCCEA
C7EBF8
E9F6FB
00AB8E
00BBA5
67D7C9
C6EFE9
E9F9F6
EB3D1F
EC4F4E
F09395
F8D3D4
FCEDEE

Requirements
Must have
• Must be Double Sided
Nice to have
• Newer Modern look with a Masculine Feel

```html
<!DOCTYPE html>
<html lang="en">
<head>
<meta charset="utf-8">
<title>Bodywork by Delmar – Business Card</title>
<link href="https://fonts.googleapis.com/css2?family=Poppins:wght@400;500;600&family=Oswald:wght@600&display=swap" rel="stylesheet">
<style>
  :root {
    --blue-deep: #0054AA;
    --blue-mid: #0677BA;
    --blue-bright: #0094D4;
    --blue-cyan: #00A9DD;
    --blue-soft: #6FCCEA;
    --blue-pale: #C7EBF8;
    --red: #EB3D1F;
    --red-light: #EC4F4E;
    --red-faint: #F8D3D4;
    --ink: #1d2430;
    --card: #F6F7F8;
    --stage: #D9DBDE;
  }
  * { box-sizing: border-box; margin: 0; padding: 0; }
  html, body { width: 1200px; height: 800px; overflow: hidden; }
  body { background: var(--stage); font-family: "Poppins", sans-serif; position: relative; }

  .card {
    position: absolute; left: 290px; width: 620px; height: 354px;
    background: var(--card); border-radius: 20px; overflow: hidden;
    border-bottom: 3px solid var(--blue-bright);
    box-shadow: 0 8px 22px rgba(0,0,0,.18);
  }
  .card--front { top: 24px; }
  .card--back { top: 414px; }

  /* front */
  .front-illustration {
    position: absolute; right: 0; top: 0; width: 240px; height: 354px;
    background: linear-gradient(160deg, var(--blue-pale) 0%, var(--blue-soft) 45%, var(--blue-cyan) 100%);
  }
  .brand { position: absolute; left: 40px; top: 72px; display: flex; align-items: center; gap: 12px; }
  .brand__dot { width: 50px; height: 50px; border-radius: 50%; background: var(--blue-bright); flex: none; }
  .brand__name { font-size: 22px; font-weight: 500; color: var(--blue-mid); letter-spacing: .02em; white-space: nowrap; }
  .person { position: absolute; left: 40px; top: 168px; }
  .person__name { font-size: 24px; font-weight: 600; color: var(--blue-bright); line-height: 1.1; }
  .person__role { font-size: 13px; font-weight: 500; color: var(--ink); margin-bottom: 14px; }
  .contact { list-style: none; }
  .contact li { display: flex; align-items: center; gap: 9px; font-size: 13px; color: var(--ink); line-height: 1.7; }
  .contact svg { width: 15px; height: 15px; flex: none; }

  /* back */
  .back-illustration {
    position: absolute; left: 0; top: 0; width: 260px; height: 354px;
    background: linear-gradient(200deg, var(--blue-mid) 0%, var(--blue-deep) 60%, var(--blue-mid) 100%);
  }
  .promo-title {
    position: absolute; left: 300px; top: 62px; width: 290px; text-align: center;
    font-size: 26px; font-weight: 500; line-height: 1.05; color: var(--blue-deep);
    text-transform: uppercase;
  }
  .offer-lead {
    position: absolute; left: 300px; top: 188px;
    font-family: "Oswald", sans-serif; font-weight: 600; font-size: 24px; color: var(--red);
    text-transform: uppercase; letter-spacing: .02em;
  }
  .punch-row { position: absolute; left: 296px; top: 234px; display: flex; gap: 10px; }
  .punch {
    width: 58px; height: 58px; border-radius: 50%; border: 3px solid var(--red-light);
    display: flex; align-items: center; justify-content: center;
    font-size: 30px; font-weight: 600; color: var(--red-faint);
  }
  .offer-badge {
    position: absolute; left: 508px; top: 172px; width: 96px; height: 96px; border-radius: 50%;
    background: var(--red);
    color: #fff; text-align: center; display: flex; flex-direction: column; justify-content: center;
    line-height: 1; text-transform: uppercase;
  }
  .offer-badge__top { font-size: 12px; font-weight: 500; }
  .offer-badge__big { font-size: 28px; font-weight: 600; }
  .offer-badge__bottom { font-size: 14px; font-weight: 500; }
</style>
</head>
<body>

<section class="card card--front" aria-label="Business card front">
  <div class="front-illustration" role="img" aria-label="Illustration area: male anatomy figure seen from behind with highlighted spine"></div>
  <div class="brand">
    <span class="brand__dot"></span>
    <span class="brand__name">Bodywork by Delmar</span>
  </div>
  <div class="person">
    <p class="person__name">Delmar Hollis</p>
    <p class="person__role">Massage Therapist</p>
    <ul class="contact">
      <li>
        <svg viewBox="0 0 16 16"><circle cx="8" cy="8" r="8" fill="var(--blue-bright)"/><path d="M5.5 4.5l1.5 1.6-.8 1c.6 1.2 1.4 2 2.6 2.6l1-.8 1.6 1.5-.9 1.1C7.8 11.3 4.7 8.2 4.4 5.4z" fill="#fff"/></svg>
        (555)-418-2073
      </li>
      <li>
        <svg viewBox="0 0 16 16"><circle cx="8" cy="8" r="8" fill="var(--blue-bright)"/><rect x="4" y="5.2" width="8" height="5.6" rx=".8" fill="#fff"/><path d="M4.3 5.6L8 8.4l3.7-2.8" stroke="var(--blue-bright)" stroke-width=".9" fill="none"/></svg>
        bodyworkbydelmar@quillmail.test
      </li>
      <li>
        <svg viewBox="0 0 16 16"><circle cx="8" cy="8" r="8" fill="var(--blue-bright)"/></svg>
        @Gr4in_bodywork
      </li>
    </ul>
  </div>
</section>

<section class="card card--back" aria-label="Business card back">
  <div class="back-illustration" role="img" aria-label="Illustration area: body figure bending forward with knee and ankle pressure points"></div>
  <h2 class="promo-title">Mobile sessions available upon request</h2>
  <p class="offer-lead">Book 3 massages</p>
  <div class="punch-row">
    <span class="punch">1</span>
    <span class="punch">2</span>
    <span class="punch">3</span>
  </div>
  <div class="offer-badge">
    <span class="offer-badge__top">Get 4th</span>
    <span class="offer-badge__big">50%</span>
    <span class="offer-badge__bottom">Off</span>
  </div>
</section>

</body>
</html>
```